Post storm repair flyer

looking for an eye catching 6x9 postcard to send out to single family home owners advertising a "Post Storm Repair Special" explaining that after the recent hurricanes its very important to have your roof checked and any repairs fixed right away before they become a bigger more costly problem and that even though your home wasn't directly hit by the storm the high wind gust could've cause unseen damage.
offer $200 off any repair *some rules may apply
Lark Roofing
888.417.LARK
www.LarkRoofing.example

Roofing

```html
<!DOCTYPE html>
<html lang="en">
<head>
<meta charset="utf-8">
<title>Post Storm Repair Special – Lark Roofing</title>
<link href="https://fonts.googleapis.com/css2?family=Poppins:wght@400;500;800;900&display=swap" rel="stylesheet">
<style>
  :root {
    --gold: #e8ad22;
    --ink: #0d0d0d;
    --paper: #f2f2f2;
    --stage: #b9b9b9;
    --white: #ffffff;
    --slate: #5c6370;
  }
  html, body {
    margin: 0;
    width: 900px;
    height: 1200px;
    overflow: hidden;
    background: var(--stage);
    font-family: "Poppins", sans-serif;
  }
  .postcard-frame {
    position: absolute;
    left: 20px;
    top: 313px;
    width: 860px;
    height: 573px;
    box-shadow: 0 4px 10px rgba(0,0,0,.25);
  }
  .postcard {
    position: absolute;
    left: 0; top: 0;
    width: 1260px;
    height: 840px;
    transform: scale(0.68254);
    transform-origin: 0 0;
    overflow: hidden;
    background: var(--paper);
  }
  .postcard > svg {
    position: absolute;
    inset: 0;
  }
  .headline {
    position: absolute;
    left: 52px;
    top: 62px;
    margin: 0;
    font-weight: 900;
    color: var(--ink);
    line-height: 1;
    letter-spacing: -2px;
  }
  .headline .line-one { display: block; font-size: 92px; }
  .headline .line-two { display: block; font-size: 84px; margin-top: 14px; }
  .headline .accent { color: var(--gold); }
  .pitch {
    position: absolute;
    left: 53px;
    top: 266px;
    width: 625px;
    margin: 0;
    font-size: 26.5px;
    line-height: 32.7px;
    font-weight: 500;
    color: var(--ink);
  }
  .pitch .row {
    display: block;
    white-space: nowrap;
    text-align: left;
  }
  .pitch .row.full {
    text-align: justify;
    text-align-last: justify;
  }
  .call-bar {
    position: absolute;
    left: 53px;
    top: 622px;
    width: 350px;
    height: 45px;
    background: var(--ink);
    display: flex;
    align-items: center;
  }
  .call-bar .phone-tab {
    width: 66px;
    height: 45px;
    background: var(--gold);
    display: flex;
    align-items: center;
    justify-content: center;
    clip-path: polygon(0 0, 80% 0, 100% 100%, 0 100%);
  }
  .call-bar .call-label {
    color: var(--white);
    font-size: 27px;
    font-weight: 500;
    margin-left: 26px;
  }
  .phone-number {
    position: absolute;
    left: 53px;
    top: 680px;
    margin: 0;
    font-size: 47px;
    font-weight: 900;
    color: var(--ink);
    letter-spacing: 0.5px;
  }
  .web-address {
    position: absolute;
    left: 58px;
    top: 748px;
    margin: 0;
    font-size: 28px;
    font-weight: 500;
    color: var(--ink);
  }
  .offer {
    position: absolute;
    left: 532px;
    top: 618px;
    width: 360px;
    text-align: center;
    line-height: 1;
    font-weight: 900;
  }
  .offer .amount { display: block; color: var(--white); font-size: 72px; }
  .offer .off { display: block; color: var(--gold); font-size: 82px; margin-top: 2px; }
  .offer .terms-mark { display: block; color: var(--gold); font-size: 26px; margin-top: 6px; letter-spacing: -0.5px; }
  .fine-print {
    position: absolute;
    left: 796px;
    top: 747px;
    width: 156px;
    height: 16px;
    line-height: 16px;
    text-align: center;
    transform: rotate(90deg);
    transform-origin: 50% 50%;
    color: var(--white);
    font-size: 12px;
    white-space: nowrap;
  }
  .brand-name {
    position: absolute;
    left: 960px;
    top: 776px;
    width: 270px;
    text-align: center;
    margin: 0;
    color: var(--white);
    font-size: 22px;
    font-weight: 500;
    letter-spacing: 0.5px;
  }
</style>
</head>
<body>
  <div class="postcard-frame">
    <article class="postcard">
      <svg width="1260" height="840" viewBox="0 0 1260 840">
        <defs>
          <linearGradient id="rooftopWash" x1="0" y1="0" x2="1" y2="1">
            <stop offset="0" stop-color="#e4e4e0"/>
            <stop offset="0.5" stop-color="#f1f1f1"/>
            <stop offset="1" stop-color="#e2e3e5"/>
          </linearGradient>
          <linearGradient id="shingleTone" x1="0" y1="0" x2="1" y2="1">
            <stop offset="0" stop-color="#6a717c"/>
            <stop offset="0.5" stop-color="#8c9097"/>
            <stop offset="1" stop-color="#4f5660"/>
          </linearGradient>
        </defs>
        <rect class="backdrop-photo" width="1260" height="840" fill="url(#rooftopWash)" role="img" aria-label="Faded photo of a shingled house roof with trees behind"/>
        <polygon class="damage-photo" points="755,325 1107,118 1260,210 1260,840 755,840" fill="url(#shingleTone)" role="img" aria-label="Close-up photo of storm-damaged asphalt shingles with torn patches"/>
        <polygon class="roof-chevron" points="835,77 892,77 892,195 1107,50 1260,140 1260,208 1107,118 835,272" fill="var(--gold)"/>
        <polyline points="835,280 1107,124 1260,214" fill="none" stroke="var(--white)" stroke-width="4"/>
        <polygon class="house-outline" points="695,268 743,243 743,495 945,635 945,840 477,840 477,635 695,495" fill="var(--gold)"/>
        <polygon class="house-badge" points="712,565 892,673 892,840 532,840 532,673" fill="var(--ink)" stroke="var(--white)" stroke-width="4"/>
      </svg>

      <h1 class="headline">
        <span class="line-one">POST <span class="accent">STORM</span></span>
        <span class="line-two">REPAIR SPECIAL</span>
      </h1>

      <p class="pitch">
        <span class="row">After the recent hurricanes its very</span>
        <span class="row">important to have your roof checked and</span>
        <span class="row full">any repairs fixed right away before they</span>
        <span class="row full">become a bigger more costly problem and</span>
        <span class="row full">that even though your home wasn't directly</span>
        <span class="row full">hit by the storm the high wind gust could've</span>
        <span class="row">cause unseen damage.</span>
      </p>

      <div class="call-bar">
        <span class="phone-tab">
          <svg width="26" height="26" viewBox="0 0 24 24"><path d="M6.6 10.8a15.1 15.1 0 0 0 6.6 6.6l2.2-2.2a1 1 0 0 1 1-.25 11.4 11.4 0 0 0 3.6.57 1 1 0 0 1 1 1V20a1 1 0 0 1-1 1A17 17 0 0 1 3 4a1 1 0 0 1 1-1h3.5a1 1 0 0 1 1 1c0 1.25.2 2.45.57 3.57a1 1 0 0 1-.25 1z" fill="var(--ink)"/></svg>
        </span>
        <span class="call-label">CALL US TODAY!</span>
      </div>
      <p class="phone-number">888.417.LARK</p>
      <p class="web-address">www.LarkRoofing.example</p>

      <div class="offer">
        <span class="amount">$200</span>
        <span class="off">OFF</span>
        <span class="terms-mark">ANY REPAIR*</span>
      </div>
      <span class="fine-print">*some rules may apply</span>

      <p class="brand-name">LARKROOFING.EXAMPLE</p>
    </article>
  </div>
</body>
</html>
```